Commercial Real Estate Company Needs an Awesome Flyer Design for their Oceanfront Property

We need a 2-page flyer or our Class A Oceanfront Property in Santa Monica, California. Approximately 16,149 square feet of Class A rare oceanfront office space with private balconies will be in available 4th Quarter of 2014. The SPACE has not been on the market for over 20 YEARS!

I attached our Previous 2-page flyer for the 2,353 square feet. We need a new vibrant, modern flyer that will attract Tech, Entertainment, Financial, and Marketing Companies to our building. Also, the 2nd Floor Space Plan is attached.

Also, please check out our website www.verlindeproperty.com. We would like to use the colors of our website and logo to incorporate with the flyer.

I updated the Must Have's on the Listing!

Target Market(s)

Entertainment, Financial, Tech Companies

Industry/Entity Type

Real Estate

Requirements
Must have
• Our Company Logo, Company, Leasing Agents On the First and 2nd Page

Trevor L. Ashdown (310) 555-0142
trev@verlindeproperty.com

Mark Oda (310) 555-0187
mark@verlindeproperty.com

Verlinde Property.
5127 N Harlow Ave, Suite 210
West Hollywood, Ca. 90069
(310) 555-0142
www.verlindeproperty.com

Also, the Front Page should indicate

"Rare Class A Oceanfront Office Space in the heart of Santa Monica"
"2nd Floor Office Space consisting of 16,159 square feet with private balconies."
Nice to have
• Please use description of the office building. You can omit whatever you think is unnecessary

"Bellhaven Court is one of Santa Monica's rare commercial properties that is both strategically located in the city's burgeoning central business district, yet ideally positioned on palm-lined Ocean Ave directly across from the Pacific Ocean. Built in 1987, the 3-story mixed-use commercial and retail property features prestigious retail Tenants such as Kelp Tavu and Dune Kitchen."

"A year-round coastal Mediterranean climate, a highly diverse business sector, and the vibrant, pedestrian-oriented Linden Row Walkway and Harbor Crest Arcade makes this beachside community a highly desirable commercial and retail location."

```html
<!DOCTYPE html>
<html lang="en">
<head>
<meta charset="utf-8">
<title>Bellhaven Court – Available Properties</title>
<link rel="stylesheet" href="https://fonts.googleapis.com/css2?family=Roboto:wght@300;400&family=Crimson+Text:ital,wght@0,400;0,600;1,400;1,600&display=swap">
<style>
  :root {
    --brand-yellow: #f9d42f;
    --band-grey: #a6a8ab;
    --ink: #2b2b2b;
    --rule: #3a3a3a;
    --paper: #ffffff;
  }
  * { margin: 0; padding: 0; box-sizing: border-box; }
  html, body { width: 928px; height: 1200px; overflow: hidden; background: var(--paper); }
  .flyer { position: relative; width: 928px; height: 1200px; font-family: "Crimson Text", Georgia, serif; color: var(--ink); }

  .brand-bar { position: absolute; left: 0; top: 0; width: 462px; height: 91px; background: var(--brand-yellow); }
  .brand-bar__name { position: absolute; left: 18px; top: 22px; font-family: "Roboto", Arial, sans-serif; font-weight: 300; font-size: 40px; letter-spacing: 1px; color: #fff; white-space: nowrap; }
  .header-rule { position: absolute; left: 462px; top: 62px; width: 133px; height: 1px; background: var(--rule); }
  .listing-tag { position: absolute; left: 595px; top: 34px; width: 263px; height: 41px; border-left: 5px solid var(--brand-yellow); border-bottom: 5px solid var(--brand-yellow); }
  .listing-tag__text { position: absolute; left: 8px; top: 4px; font-family: "Roboto", Arial, sans-serif; font-weight: 300; font-size: 25px; color: var(--ink); white-space: nowrap; }

  .title-band { position: absolute; left: 0; top: 110px; width: 326px; height: 50px; background: var(--band-grey); }
  .title-band__name { position: absolute; left: 57px; top: 4px; font-style: italic; font-weight: 400; font-size: 35px; line-height: 42px; color: #1c1c1c; white-space: nowrap; }
  .site-address { position: absolute; left: 57px; top: 168px; font-style: normal; font-size: 22px; line-height: 27px; color: #444; }

  .brand-mark { position: absolute; text-align: center; font-family: "Roboto", Arial, sans-serif; font-weight: 400; color: #111; }
  .brand-mark__dot { display: block; margin: 0 auto; border-radius: 50%; background: var(--brand-yellow); }
  .brand-mark--small { left: 390px; top: 120px; width: 150px; font-size: 12px; line-height: 15px; letter-spacing: 3px; }
  .brand-mark--small .brand-mark__dot { width: 44px; height: 44px; margin-bottom: 16px; }
  .brand-mark--large { left: 340px; top: 862px; width: 290px; font-size: 25px; line-height: 30px; letter-spacing: 5px; }
  .brand-mark--large .brand-mark__dot { width: 120px; height: 120px; margin-bottom: 32px; }

  .photo { position: absolute; }
  .photo--hero { left: 57px; top: 238px; width: 558px; height: 312px; background: linear-gradient(180deg, #2e57a8 0%, #6a8fc9 45%, #d9d6cc 62%, #8c8f88 100%); box-shadow: 6px 8px 8px rgba(0,0,0,0.35); }
  .photo--side { left: 637px; width: 234px; border: 1px solid #222; }
  .photo--terrace { top: 155px; height: 400px; background: linear-gradient(180deg, #7ea6d8 0%, #c9c6bd 45%, #6f8a54 80%, #4f5d3a 100%); }
  .photo--office { top: 578px; height: 156px; background: linear-gradient(135deg, #ede6d2 0%, #d6cdb4 60%, #8a8377 100%); }
  .photo--floor { top: 756px; height: 156px; background: linear-gradient(180deg, #f1eee6 0%, #d8c8a4 55%, #8b8a86 100%); }
  .photo--lobby { top: 933px; height: 177px; background: linear-gradient(180deg, #6d6f72 0%, #9c9ea0 55%, #8a2a2a 100%); }

  .description { position: absolute; left: 57px; top: 580px; width: 560px; font-size: 14.6px; line-height: 23px; color: #333; }
  .description p + p { margin-top: 12px; }
  .description em { font-weight: 600; }

  .offer { position: absolute; left: 57px; top: 760px; width: 558px; color: #1c1c1c; }
  .offer__headline { font-style: italic; font-weight: 600; font-size: 17px; line-height: 22px; }
  .offer__detail { font-size: 15px; line-height: 20px; }

  .section-rule { position: absolute; left: 57px; top: 810px; width: 558px; height: 1px; background: var(--rule); }

  .contacts { position: absolute; left: 57px; top: 840px; font-size: 17px; line-height: 21.5px; color: #111; }
  .contacts__group + .contacts__group { margin-top: 23px; }

  .footer-band { position: absolute; left: 0; top: 1127px; width: 928px; height: 73px; background: var(--band-grey); }
  .footer-band__url { display: block; text-align: center; padding-top: 18px; font-size: 24px; color: #1c1c1c; }
</style>
</head>
<body>
<div class="flyer">
  <header>
    <div class="brand-bar"><span class="brand-bar__name">VERLINDE PROPERTY</span></div>
    <div class="header-rule"></div>
    <div class="listing-tag"><span class="listing-tag__text">available PROPERTIES</span></div>
  </header>

  <div class="title-band"><h1 class="title-band__name">Bellhaven Court</h1></div>
  <address class="site-address">1750 Shoreline Avenue<br>Santa Monica, CA 90401</address>

  <div class="brand-mark brand-mark--small"><span class="brand-mark__dot"></span>VERLINDE<br>PROPERTY</div>

  <div class="photo photo--hero" role="img" aria-label="Photo of the three-story white building with palm trees on Ocean Avenue"></div>
  <div class="photo photo--side photo--terrace" role="img" aria-label="Photo of the balcony walkway with palm trees and ocean view"></div>
  <div class="photo photo--side photo--office" role="img" aria-label="Photo of an empty office with windows onto palm trees"></div>
  <div class="photo photo--side photo--floor" role="img" aria-label="Photo of an open office floor with reception desk and cubicles"></div>
  <div class="photo photo--side photo--lobby" role="img" aria-label="Photo of the elevator lobby with grey panels and red mats"></div>

  <section class="description">
    <p><em>Bellhaven Court</em> is one of Santa Monica’s rare commercial properties that is both strategically located in the city’s burgeoning central business district, yet ideally positioned on palm-lined Ocean Ave directly across from the Pacific Ocean. Built in 1987, the 3-story mixed-use commercial and retail property features prestigious retail Tenants such as Kelp Tavu and Dune Kitchen.</p>
    <p>A year-round coastal Mediterranean climate, a highly diverse business sector, and the vibrant, pedestrian-oriented Linden Row Walkway and Harbor Crest Arcade makes this beachside community a highly desirable commercial and retail location.</p>
  </section>

  <section class="offer">
    <h2 class="offer__headline">Rare Class A Oceanfront Office Space in the heart of Santa Monica</h2>
    <p class="offer__detail">2nd Floor Office Space consisting of 16,159 square feet with private balconies.</p>
  </section>

  <div class="section-rule"></div>

  <section class="contacts">
    <div class="contacts__group">Trevor L. Ashdown (310) 555-0142<br>trev@verlindeproperty.com</div>
    <div class="contacts__group">Mark Oda (310) 555-0187<br>mark@verlindeproperty.com</div>
    <div class="contacts__group">Verlinde Property.<br>5127 N Harlow Ave, Suite 210<br>West Hollywood, Ca. 90069<br>(310) 555-0142</div>
  </section>

  <div class="brand-mark brand-mark--large"><span class="brand-mark__dot"></span>VERLINDE<br>PROPERTY</div>

  <footer class="footer-band"><span class="footer-band__url">www.verlindeproperty.com</span></footer>
</div>
</body>
</html>
```